Mesh Banner Design for Business Premises

We require the design of a large mesh banner to be installed across the front fence of our warehouse. The banner should prominently feature our existing Rigmore logo and brand colours (yellow, white, and black) and be designed to be highly visible from the road.

The overall aesthetic should be strong, masculine, and industrial, reflecting the nature of the scaffolding and construction industry. The background should be predominantly black, with our branding incorporated in yellow and white for strong contrast and readability.

The banner should clearly communicate the full scope of services we provide, including:

Scaffold Design
Scaffold Engineering
Scaffold Installation / Erection
Scaffold Dismantling

It should also indicate the types of projects and clients we service, including:

Commercial
Industrial
Residential
Civil

The design should feel bold and professional, with a construction-oriented style that aligns with the scaffolding industry. It should be clean, impactful, and easy to read from a distance, ensuring passing traffic can quickly understand our services.

Where possible, subtle industrial or structural design elements (such as scaffold components, steel textures, or linework) may be incorporated into the background to reinforce the industry theme while keeping the layout uncluttered.

The final design will be produced as a large-format mesh banner for outdoor installation, so it should be created with this application and viewing distance in mind.

```html
<!DOCTYPE html>
<html lang="en">
<head>
<meta charset="utf-8">
<title>Rigmore Mesh Banner</title>
<link href="https://fonts.googleapis.com/css2?family=Exo+2:wght@600;700;800&display=swap" rel="stylesheet">
<style>
  :root {
    --page: #ffffff;
    --black: #121212;
    --steel-dark: #1a1a1a;
    --steel-mid: #2e2e2e;
    --yellow: #f2b01e;
    --gold: #d9a63a;
    --white: #f4f4f4;
  }
  html, body {
    margin: 0;
    padding: 0;
    width: 1200px;
    height: 799px;
    overflow: hidden;
    background: var(--page);
  }
  .banner {
    position: absolute;
    left: 41px;
    top: 171px;
    width: 1121px;
    height: 427px;
    background: var(--black);
    overflow: hidden;
  }
  .banner-backdrop {
    position: absolute;
    inset: 0;
    background: radial-gradient(ellipse at 55% 35%, var(--steel-mid) 0%, var(--steel-dark) 55%, var(--black) 100%);
  }
  .brand {
    position: absolute;
    left: 52px;
    top: 118px;
    display: flex;
    align-items: center;
    gap: 26px;
  }
  .brand-square {
    width: 56px;
    height: 56px;
    background: var(--yellow);
  }
  .brand-name {
    font-family: "Exo 2", sans-serif;
    font-weight: 700;
    font-size: 42px;
    letter-spacing: 3px;
    color: var(--white);
    margin: 0;
    line-height: 1;
  }
  .services {
    position: absolute;
    left: 664px;
    top: 46px;
    margin: 0;
    padding: 0;
    list-style: none;
  }
  .service {
    display: flex;
    align-items: center;
    height: 47.5px;
    font-family: "Exo 2", sans-serif;
    font-weight: 600;
    font-size: 27px;
    color: var(--white);
    white-space: nowrap;
  }
  .service-small { font-size: 23px; }
  .service-arrow {
    width: 28px;
    height: 18px;
    margin-right: 12px;
    flex: none;
  }
  .hazard-band {
    position: absolute;
    height: 9px;
    background: var(--gold);
  }
  .hazard-band--top { left: 642px; top: 248px; width: 479px; }
  .hazard-band--mid { left: 173px; top: 361px; width: 792px; }
  .hazard-band--low { left: 182px; top: 401px; width: 156px; }
  .hazard-diagonal {
    position: absolute;
    left: 0;
    top: 0;
    width: 1121px;
    height: 427px;
  }
  .phone-ribbon {
    position: absolute;
    left: 40px;
    top: 256px;
    width: 564px;
    height: 90px;
  }
  .phone-ribbon svg { position: absolute; inset: 0; }
  .phone-number {
    position: absolute;
    inset: 0;
    display: flex;
    align-items: center;
    justify-content: center;
    gap: 16px;
    margin: 0;
    font-family: "Exo 2", sans-serif;
    font-weight: 800;
    font-size: 50px;
    color: var(--white);
  }
  .phone-accent { color: var(--yellow); }
  .sectors {
    position: absolute;
    left: 624px;
    top: 272px;
    width: 460px;
    margin: 0;
    text-align: center;
    font-family: "Exo 2", sans-serif;
    font-weight: 700;
    font-size: 24px;
    line-height: 32px;
    letter-spacing: 0.5px;
    color: var(--gold);
  }
  .sector-divider { color: var(--white); font-weight: 600; padding: 0 6px; }
</style>
</head>
<body>
  <main class="banner">
    <div class="banner-backdrop" role="img" aria-label="Dark photograph of steel scaffolding structures"></div>

    <div class="brand">
      <span class="brand-square"></span>
      <h1 class="brand-name">RIGMORE</h1>
    </div>

    <ul class="services">
      <li class="service"><svg class="service-arrow" viewBox="0 0 28 18"><path d="M2 2 L10 9 L2 16 M14 2 L22 9 L14 16" fill="none" stroke="#f2b01e" stroke-width="4"/></svg>Scaffold Design</li>
      <li class="service"><svg class="service-arrow" viewBox="0 0 28 18"><path d="M2 2 L10 9 L2 16 M14 2 L22 9 L14 16" fill="none" stroke="#f2b01e" stroke-width="4"/></svg>Scaffold Engineering</li>
      <li class="service"><svg class="service-arrow" viewBox="0 0 28 18"><path d="M2 2 L10 9 L2 16 M14 2 L22 9 L14 16" fill="none" stroke="#f2b01e" stroke-width="4"/></svg>Scaffold Installation&nbsp;<span class="service-small">/ Erection</span></li>
      <li class="service"><svg class="service-arrow" viewBox="0 0 28 18"><path d="M2 2 L10 9 L2 16 M14 2 L22 9 L14 16" fill="none" stroke="#f2b01e" stroke-width="4"/></svg>Scaffold Dismantling</li>
    </ul>

    <div class="hazard-band hazard-band--top"></div>
    <div class="hazard-band hazard-band--mid"></div>
    <div class="hazard-band hazard-band--low"></div>
    <svg class="hazard-diagonal" viewBox="0 0 1121 427" width="1121" height="427">
      <polygon points="876,427 906,427 1121,322 1121,304" fill="#d9a63a"/>
    </svg>

    <div class="phone-ribbon">
      <svg viewBox="0 0 564 90" width="564" height="90">
        <rect x="34" y="8" width="496" height="74" fill="#151515" stroke="#f2b01e" stroke-width="3"/>
        <path d="M2 8 L30 45 L2 82 M14 8 L42 45 L14 82" fill="none" stroke="#f2b01e" stroke-width="4"/>
        <path d="M562 8 L534 45 L562 82 M550 8 L522 45 L550 82" fill="none" stroke="#f2b01e" stroke-width="4"/>
      </svg>
      <p class="phone-number"><span>1300</span><span class="phone-accent">7 RIGUP</span></p>
    </div>

    <p class="sectors">
      COMMERCIAL<span class="sector-divider">|</span>INDUSTRIAL<br>
      RESIDENTIAL<span class="sector-divider">|</span>CIVIL
    </p>
  </main>
</body>
</html>
```